Business Card: RW Office Partners - Your organised problem solver

Business Name: RW Office Partners
Website: www.rwofficepartners-example.com.au
Email: maribel@rwofficepartners-example.com.au
Mobile: 61 400 000 000
Facebook: @rwofficepartners
Instrgram: @rwofficepartners

Brading Colours:
HEX
#986474
#ddccd3
#7a8498
#c9d8e4
#000000
#ffffff

Tag Line: Your organised problem solver

Link to DRAFT website:
https://draftsites-example.com/rw-office-partners

About Page from the website:
My name is Maribel Rowe, and I would love to assist you to become more productive in your day to day and achieve your business and personal goals.
My mission is to give you time, time to work on the important tasks of your business or to be able to spend more time with your family. I will take on the tasks you don’t have time for, don’t know well or simply don’t like to do.
I have an extensive background in Administration, Tender Coordination, Document Control, WHS and Quality Management working primarily in the Construction, Mining and Corporate World.
I am passionate about being organised, having order and making things in your life (and mine) easier! I love to watch something unfold and grow into something amazing! I am known for being the go-to problem solver, the organiser of all things, producing high standards of work even under pressure. I’m also a confident communicator, and I understand that you’re busy running your business.

Target Market(s)

Small to Medium Business who require assistance in their business by a virtual assistant.

Industry/Entity Type

Virtual Assistant

Contact Information for Business Card

Mobile: 61 400 000 000

Font styles to use
Sans Serif

Colors
ffffff

Requirements
Must have
• Branding Colours as outlined.
Contact Details as outlined.
Logo as provided.
Proper contact details - mobile, facebook, instragm, website.
Simple, Elegant, very clean looking.
Should not have
• Note cute with pictures.
Not too girly as still want to market to construction companies.

```html
<!DOCTYPE html>
<html lang="en">
<head>
<meta charset="UTF-8">
<title>RW Office Partners – Business Card</title>
<link rel="stylesheet" href="https://fonts.googleapis.com/css2?family=Montserrat:wght@500;600&family=Open+Sans:wght@400&display=swap">
<style>
  :root {
    --brand-plum: #986474;
    --brand-blush: #ddccd3;
    --brand-slate: #7a8498;
    --brand-mist: #c9d8e4;
    --ink: #000000;
    --paper: #ffffff;
    --stage: #e6e6e8;
    --divider: #b9b9bd;
  }
  * { box-sizing: border-box; margin: 0; padding: 0; }
  html, body {
    width: 1200px; height: 1015px; overflow: hidden;
    background: var(--stage);
  }
  .canvas {
    position: relative; width: 1200px; height: 1015px;
  }
  .card {
    position: absolute; left: 250px; width: 700px; height: 400px;
    overflow: hidden;
    box-shadow: 0 6px 18px rgba(0,0,0,0.18);
  }

  /* Back of card */
  .card-back { top: 90px; background: var(--brand-plum); }
  .monogram-pattern {
    position: absolute; inset: 0;
    background: linear-gradient(135deg, #9c6979 0%, var(--brand-plum) 55%, #93606f 100%);
  }
  .back-name {
    position: absolute; right: 88px; top: 118px;
    font-family: "Montserrat", sans-serif; font-weight: 600;
    font-size: 30px; letter-spacing: 0.5px; color: var(--paper);
    white-space: nowrap;
  }
  .back-tagline {
    position: absolute; left: 0; right: 0; top: 258px; text-align: center;
    font-family: "Montserrat", sans-serif; font-weight: 600;
    font-size: 17px; letter-spacing: 0.6px; text-transform: uppercase;
    color: var(--paper); white-space: nowrap;
  }

  /* Front of card */
  .card-front { top: 525px; background: var(--paper); }
  .front-brand {
    position: absolute; left: 60px; top: 196px; width: 240px;
    font-family: "Montserrat", sans-serif; font-weight: 600;
    font-size: 26px; line-height: 1.15; color: var(--brand-plum);
    text-transform: uppercase; letter-spacing: 0.5px;
  }
  .front-divider {
    position: absolute; left: 310px; top: 112px; width: 1.5px; height: 158px;
    background: var(--divider);
  }
  .contact-list {
    position: absolute; left: 330px; right: 20px; top: 112px; list-style: none;
    font-family: "Open Sans", sans-serif; font-size: 14.5px; line-height: 1.2;
    color: var(--ink);
  }
  .contact-item {
    display: flex; align-items: center; gap: 9px; height: 26px;
    white-space: nowrap;
  }
  .contact-item svg { width: 15px; height: 15px; flex: none; }
  .contact-item.social-first { margin-top: 22px; }
  .social-dot {
    width: 20px; height: 20px; border-radius: 50%;
    border: 1.4px solid var(--brand-slate); flex: none;
  }
  .contact-item.social { height: 28px; }
  .band-plum {
    position: absolute; left: 0; bottom: 0; width: 378px; height: 18px;
    background: var(--brand-plum);
  }
  .band-slate {
    position: absolute; right: 0; bottom: 0; width: 322px; height: 30px;
    background: var(--brand-slate);
  }
</style>
</head>
<body>
<main class="canvas">

  <section class="card card-back" aria-label="Business card back">
    <div class="monogram-pattern" role="img" aria-label="Faint repeated brand monogram pattern across the card"></div>
    <div class="back-name">RW Office Partners</div>
    <p class="back-tagline">Your organised problem solver</p>
  </section>

  <section class="card card-front" aria-label="Business card front">
    <div class="front-brand">RW Office Partners</div>
    <div class="front-divider"></div>
    <ul class="contact-list">
      <li class="contact-item">
        <svg viewBox="0 0 16 16"><path fill="#986474" d="M3 2h3l1.3 3.2-1.7 1.2a8 8 0 0 0 4 4l1.2-1.7L14 10v3a1.5 1.5 0 0 1-1.5 1.5A11 11 0 0 1 1.5 3.5 1.5 1.5 0 0 1 3 2z"/></svg>
        <span>61 400 000 000</span>
      </li>
      <li class="contact-item">
        <svg viewBox="0 0 16 16"><rect x="1" y="3" width="14" height="10" rx="1" fill="#986474"/><path d="M1.5 3.8 8 9l6.5-5.2" fill="none" stroke="#fff" stroke-width="1.3"/></svg>
        <span>maribel@rwofficepartners-example.com.au</span>
      </li>
      <li class="contact-item">
        <svg viewBox="0 0 16 16"><circle cx="8" cy="8" r="7" fill="#986474"/><path d="M1 8h14M8 1c-3 3.5-3 10.5 0 14M8 1c3 3.5 3 10.5 0 14" fill="none" stroke="#fff" stroke-width="1"/></svg>
        <span>www.rwofficepartners-example.com.au</span>
      </li>
      <li class="contact-item social social-first">
        <span class="social-dot"></span>
        <span>@rwofficepartners</span>
      </li>
      <li class="contact-item social">
        <span class="social-dot"></span>
        <span>@rwofficepartners</span>
      </li>
    </ul>
    <div class="band-plum"></div>
    <div class="band-slate"></div>
  </section>

</main>
</body>
</html>
```